Redfield interiors PTY LTD

My business specializes in commercial fitout which builds walls, ceilings, doors, uses also materials aluminium in works. Id like to have a logo designed for my company too.

Industry/Entity Type

Business

```html
<!DOCTYPE html>
<html lang="en">
<head>
<meta charset="utf-8">
<title>Redfield Interiors – Business Card</title>
<link href="https://fonts.googleapis.com/css2?family=Montserrat:wght@400;600&family=Open+Sans:ital,wght@0,400;1,700&display=swap" rel="stylesheet">
<style>
  :root {
    --backdrop: #3a3b3d;
    --card: #1d1e20;
    --card-edge: #141516;
    --accent: #1a80d6;
    --ink: #e9eaec;
    --muted: #2b2c2f;
  }
  * { box-sizing: border-box; margin: 0; padding: 0; }
  html, body {
    width: 799px; height: 1200px; overflow: hidden;
    background: var(--backdrop);
  }
  .sheet {
    position: relative; width: 799px; height: 1200px;
    display: flex; flex-direction: column; align-items: center; justify-content: space-around;
    padding: 60px 0;
  }
  .card {
    position: relative; width: 640px; height: 366px;
    background: var(--card);
    border: 1px solid var(--card-edge);
    box-shadow: 0 14px 30px rgba(0,0,0,.45);
    font-family: "Montserrat", sans-serif;
    color: var(--ink);
  }
  /* front */
  .card--front { display: flex; align-items: center; justify-content: center; }
  .front-mark {
    display: flex; align-items: center; gap: 14px;
    font-family: "Montserrat", sans-serif; font-weight: 600;
    font-size: 26px; letter-spacing: 4px; text-transform: uppercase;
    color: var(--muted);
  }
  .front-mark__dot { width: 22px; height: 22px; border-radius: 50%; background: var(--muted); }

  /* back */
  .holder { position: absolute; left: 42px; top: 66px; }
  .holder__name {
    font-family: "Open Sans", sans-serif; font-style: italic; font-weight: 700;
    font-size: 25px; line-height: 1.2; color: var(--accent);
  }
  .holder__role { font-size: 13px; margin-top: 2px; }
  .divider {
    position: absolute; left: 186px; top: 120px; width: 410px; height: 2px;
    background: var(--accent);
  }
  .contact { position: absolute; left: 42px; top: 146px; list-style: none; }
  .contact li { display: flex; align-items: center; gap: 14px; font-size: 14px; height: 24px; }
  .contact svg { width: 13px; height: 13px; fill: var(--accent); }
  .brand {
    position: absolute; right: 44px; top: 62px;
    display: flex; align-items: center; gap: 12px;
    font-family: "Montserrat", sans-serif; font-weight: 600;
    font-size: 20px; letter-spacing: 3px; text-transform: uppercase;
    color: var(--accent);
  }
  .brand__dot { width: 18px; height: 18px; border-radius: 50%; background: var(--accent); }
  .address {
    position: absolute; right: 46px; top: 236px;
    font-size: 16px; line-height: 1.45; text-align: left; font-style: normal;
  }
</style>
</head>
<body>
<main class="sheet">
  <section class="card card--front" aria-label="Card front">
    <div class="front-mark"><span class="front-mark__dot"></span>Redfield</div>
  </section>

  <section class="card card--back" aria-label="Card back">
    <div class="holder">
      <p class="holder__name">John Doe Smith</p>
      <p class="holder__role">Managing Director</p>
    </div>
    <div class="divider"></div>
    <ul class="contact">
      <li>
        <svg viewBox="0 0 16 16"><path d="M3 1h3l1.5 4-2 1.2a9 9 0 0 0 4.3 4.3L11 8.5l4 1.5v3a2 2 0 0 1-2 2A12 12 0 0 1 1 3a2 2 0 0 1 2-2z"/></svg>
        555.555.5555
      </li>
      <li>
        <svg viewBox="0 0 16 16"><path d="M1 3h14v10H1z"/><path d="M1 3h14L8 8.5z" fill="#1d1e20"/></svg>
        Johndoe@example.com
      </li>
      <li>
        <svg viewBox="0 0 16 16"><circle cx="8" cy="8" r="7"/><path d="M1 8h14M8 1c3 3 3 11 0 14M8 1c-3 3-3 11 0 14" stroke="#1d1e20" stroke-width="1.2" fill="none"/></svg>
        www.example.com
      </li>
    </ul>
    <div class="brand"><span class="brand__dot"></span>Redfield Interiors</div>
    <address class="address">234 Anywhere St.,<br>Any Town, US 123456</address>
  </section>
</main>
</body>
</html>
```